New website for existing IT services company

We are a leading IT managed services provider and cloud services provider based in Sydney, Australia.
We are looking for a fresh, modern, contemporary and functional website.
We need a certain level of dynamic capabilities, such as the option to add youtube training / blog clips. So there needs to be a CMS.
Our existing website has pages including home, about us, services, contact us. Also links for remote support and connecting to our help desk system. As well as client testimonials.
The existing website is korivel.com.au however this is only posted for informational purposes. We are looking at a complete fresh re-design
We are open to the use of illustrations, however this is not a must.
I have uploaded an eps file containing our logo.
Updates
The website needs to be functional on tablets and phones as well. Added Thursday, April 30, 2015

```html
<!DOCTYPE html>
<html lang="en">
<head>
<meta charset="utf-8">
<title>Korivel — IT Managed &amp; Cloud Services</title>
<link rel="stylesheet" href="https://fonts.googleapis.com/css2?family=Archivo+Black&family=Chivo:wght@400;700;900&display=swap">
<style>
:root{
  --blue:#1e9be0;
  --black:#111213;
  --footer:#161718;
  --hero:#3b4348;
  --hero-dark:#2e3539;
  --band:#4d5b63;
  --band-dark:#39444b;
  --white:#ffffff;
  --ink:#2a2a2a;
  --muted:#8a8a8a;
  --line:#e3e3e3;
  --widget:#e9e9e9;
  --field:#ffffff;
}
*{box-sizing:border-box;margin:0;padding:0}
html,body{width:773px;height:1200px;overflow:hidden;background:var(--white)}
body{font-family:"Chivo",Arial,sans-serif;color:var(--ink);position:relative}
a{color:inherit;text-decoration:none}

/* header */
.site-header{position:absolute;left:0;top:0;width:773px;height:56px;background:var(--black)}
.brand{position:absolute;left:57px;top:14px;display:flex;align-items:center;gap:6px;color:var(--white);font-weight:900;font-size:22px;letter-spacing:.5px}
.brand-mark{width:12px;height:12px;background:var(--blue)}
.main-nav{position:absolute;top:22px;left:0;width:773px;font-size:10px;font-weight:400;color:var(--white)}
.main-nav a{position:absolute;white-space:nowrap}
.main-nav .is-active{color:var(--blue)}
.search-icon{position:absolute;left:720px;top:20px}

/* hero */
.hero{position:absolute;left:0;top:56px;width:773px;height:383px;background:radial-gradient(ellipse at 50% 45%,var(--hero) 0%,var(--hero-dark) 100%)}
.hero-title{position:absolute;left:0;top:154px;width:773px;text-align:center;font-family:"Archivo Black",Arial,sans-serif;font-size:27px;color:var(--blue);letter-spacing:.3px}
.hero-sub{position:absolute;left:0;top:200px;width:773px;text-align:center;font-size:15px;color:var(--blue);letter-spacing:.5px}
.btn{position:absolute;display:flex;align-items:center;justify-content:center;font-family:"Archivo Black",Arial,sans-serif;font-size:8.5px;letter-spacing:1px;color:var(--white)}
.btn-solid{background:var(--blue)}
.btn-ghost{border:2px solid var(--white)}
.slider-arrow{position:absolute;width:38px;height:38px;border:2px solid var(--white);border-radius:50%;top:196px}
.slider-arrow svg{position:absolute;left:11px;top:11px}
.mail-tab{position:absolute;left:740px;top:349px;width:28px;height:27px;background:#222;display:flex;align-items:center;justify-content:center}

/* features */
.features{position:absolute;left:0;top:439px;width:773px;height:288px;background:var(--white)}
.feature{position:absolute;top:36px;width:170px;text-align:center}
.feature-icon{width:58px;height:58px;margin:0 auto;border:1px solid var(--line);border-radius:50%;display:flex;align-items:center;justify-content:center}
.feature h3{margin-top:22px;font-size:12px;font-weight:400;color:var(--ink);letter-spacing:.2px}
.feature p{margin:21px auto 0;width:140px;font-size:8.5px;line-height:13px;color:var(--muted)}
.btn-outline{position:relative;display:flex;margin:37px auto 0;width:80px;height:23px;border:1.5px solid var(--blue);align-items:center;justify-content:center;font-family:"Archivo Black",Arial,sans-serif;font-size:6.5px;letter-spacing:.8px;color:var(--blue)}

/* call to action */
.cta{position:absolute;left:0;top:727px;width:773px;height:251px;background:linear-gradient(160deg,var(--band) 0%,var(--band-dark) 100%)}
.cta h2{position:absolute;left:0;top:60px;width:773px;text-align:center;font-size:18px;font-weight:400;color:var(--white)}
.cta p{position:absolute;left:0;top:109px;width:773px;text-align:center;font-size:9px;line-height:13px;color:#c9d0d4}

/* footer */
.site-footer{position:absolute;left:0;top:978px;width:773px;height:222px;background:var(--footer);border-top:1px solid #3a6f8c}
.footer-brand{position:absolute;left:96px;top:104px;display:flex;align-items:center;gap:5px;color:var(--white);font-weight:900;font-size:21px}
.social{position:absolute;left:86px;top:146px;display:flex;gap:13px}
.social span{width:9px;height:9px;border:1.5px solid #9a9a9a;border-radius:50%}
.link-col{position:absolute;top:58px}
.link-col h4{font-family:"Archivo Black",Arial,sans-serif;font-size:7.5px;letter-spacing:.8px;color:var(--white);margin-bottom:10px}
.link-col li{list-style:none;font-size:8.5px;color:#cfcfcf;line-height:16.8px}

/* contact widget */
.contact-widget{position:absolute;left:592px;top:854px;width:177px;height:304px;background:var(--widget);box-shadow:0 0 6px rgba(0,0,0,.25);padding:14px 7px 0;text-align:center}
.contact-widget h5{font-size:6.5px;font-weight:700;letter-spacing:.8px;color:#666}
.contact-widget .intro{margin-top:6px;font-size:7.5px;line-height:11px;color:#888}
.field{margin-top:4px;background:var(--field);height:21px;text-align:left;font-size:6px;color:#888;padding:6px 6px}
.field.first{margin-top:9px}
.field.tall{height:54px}
.refresh{margin-top:9px;font-size:7px;font-weight:700;color:var(--blue)}
.captcha{margin:9px 0 0 21px;width:70px;height:22px;background:linear-gradient(90deg,#3b7fc4,#5a9bd8);border-radius:2px}
.send{margin:11px auto 0;width:42px;height:20px;background:var(--blue);color:var(--white);font-size:7px;letter-spacing:1px;display:flex;align-items:center;justify-content:center}
.chat-btn{position:absolute;left:708px;top:1166px;width:27px;height:27px;background:var(--blue);display:flex;align-items:center;justify-content:center}
.to-top{position:absolute;left:748px;top:1174px}
</style>
</head>
<body>

<header class="site-header">
  <a class="brand" href="#">KORIVEL<span class="brand-mark"></span></a>
  <nav class="main-nav">
    <a class="is-active" style="left:416px">HOME</a>
    <a style="left:471px">ABOUT</a>
    <a style="left:530px">SERVICES</a>
    <a style="left:602px">STORE</a>
    <a style="left:660px">CONTACT</a>
  </nav>
  <svg class="search-icon" width="11" height="11" viewBox="0 0 11 11"><circle cx="4.5" cy="4.5" r="3.3" fill="none" stroke="#fff" stroke-width="1.6"/><line x1="7" y1="7" x2="10" y2="10" stroke="#fff" stroke-width="1.8"/></svg>
</header>

<section class="hero" role="img" aria-label="Flat-lay desk scene with notebook, keyboard, mouse, tablet, pens and highlighter on a dark surface">
  <h1 class="hero-title">WE CRAFT AWESOME THINGS</h1>
  <p class="hero-sub">UI/UX . WEB APPS. MOBILE APPS.</p>
  <a class="btn btn-solid" style="left:277px;top:240px;width:106px;height:30px">REGISTER NOW</a>
  <a class="btn btn-ghost" style="left:391px;top:240px;width:98px;height:30px">LEARN MORE</a>
  <span class="slider-arrow" style="left:10px"><svg width="14" height="14" viewBox="0 0 14 14"><path d="M9 2 4 7l5 5" fill="none" stroke="#fff" stroke-width="1.6"/></svg></span>
  <span class="slider-arrow" style="left:724px"><svg width="14" height="14" viewBox="0 0 14 14"><path d="M5 2l5 5-5 5" fill="none" stroke="#fff" stroke-width="1.6"/></svg></span>
  <span class="mail-tab"><svg width="12" height="9" viewBox="0 0 12 9"><rect width="12" height="9" fill="#fff"/><path d="M0 0l6 5 6-5" fill="none" stroke="#222" stroke-width="1.2"/></svg></span>
</section>

<section class="features">
  <div class="feature" style="left:45px">
    <div class="feature-icon"><svg width="26" height="26" viewBox="0 0 26 26" fill="none" stroke="#1e9be0" stroke-width="1.4"><path d="M3 12 23 3 17 22 12 15Z"/><path d="M12 15 23 3"/><path d="M12 15v6l3-4"/></svg></div>
    <h3>Fast &amp; Fluent</h3>
    <p>Morbi fringilla convallis sapien, id pulvinar odio volutpat. Etiam habebis sem dicantur magna mollis euismod.</p>
    <a class="btn-outline">LEARN MORE</a>
  </div>
  <div class="feature" style="left:216px">
    <div class="feature-icon"><svg width="26" height="26" viewBox="0 0 26 26" fill="none" stroke="#1e9be0" stroke-width="1.4"><path d="M10 9V3h6v6l6 13H4Z"/><path d="M6 17h14"/><circle cx="13" cy="1.5" r="1"/></svg></div>
    <h3>Idea &amp; Research</h3>
    <p>Morbi fringilla convallis sapien, id pulvinar odio volutpat. Etiam habebis sem dicantur magna mollis euismod.</p>
    <a class="btn-outline">LEARN MORE</a>
  </div>
  <div class="feature" style="left:388px">
    <div class="feature-icon"><svg width="26" height="26" viewBox="0 0 26 26" fill="none" stroke="#1e9be0" stroke-width="1.4"><path d="M22 4c-7 0-11 5-13 10l3 3c5-2 10-6 10-13Z"/><circle cx="16" cy="10" r="1.8"/><path d="M9 14H5l3-4h4M12 17v4l4-3v-4"/><path d="M7 19l-3 3"/></svg></div>
    <h3>Performant</h3>
    <p>Morbi fringilla convallis sapien, id pulvinar odio volutpat. Etiam habebis sem dicantur magna mollis euismod.</p>
    <a class="btn-outline">LEARN MORE</a>
  </div>
  <div class="feature" style="left:558px">
    <div class="feature-icon"><svg width="26" height="26" viewBox="0 0 26 26" fill="none" stroke="#1e9be0" stroke-width="1.4"><path d="M3 13a10 9 0 0 1 20 0c-2-2-4-2-5 0-1-2-4-2-5 0-1-2-4-2-5 0-1-2-3-2-5 0Z"/><path d="M13 13v8a2 2 0 0 1-4 0"/><path d="M13 2v2"/></svg></div>
    <h3>Solid Support</h3>
    <p>Morbi fringilla convallis sapien, id pulvinar odio volutpat. Etiam habebis sem dicantur magna mollis euismod.</p>
    <a class="btn-outline">LEARN MORE</a>
  </div>
</section>

<section class="cta" role="img" aria-label="Muted photograph of a laptop keyboard behind a grey overlay">
  <h2>You need to try Lumora to see how wonderful it is</h2>
  <p>Maecenas porta arcu in metus dignissim, quis facilisis ligula bibendum.<br>Aliquam malesuada libero sit amet mi laoreet.</p>
  <a class="btn btn-solid" style="left:265px;top:178px;width:108px;height:30px">REGISTER NOW</a>
  <a class="btn btn-ghost" style="left:396px;top:178px;width:97px;height:30px">LEARN MORE</a>
</section>

<footer class="site-footer">
  <div class="footer-brand">KORIVEL<span class="brand-mark"></span></div>
  <div class="social"><span></span><span></span><span></span><span></span><span></span></div>
  <div class="link-col" style="left:247px">
    <h4>QUICK LINKS</h4>
    <ul><li>Excepteur sint obcaecat.</li><li>A communi observantia.</li><li>Cum ceteris in veneratione.</li><li>Quid securi etiam.</li><li>Hi omnes lingua, institutis.</li></ul>
  </div>
  <div class="link-col" style="left:414px">
    <h4>USEFUL LINKS</h4>
    <ul><li>Excepteur sint obcaecat.</li><li>A communi observantia.</li><li>Cum ceteris in veneratione.</li><li>Quid securi etiam.</li><li>Hi omnes lingua, institutis.</li></ul>
  </div>
  <div class="link-col" style="left:580px">
    <h4>SERVICES</h4>
    <ul><li>Excepteur sint obcaecat.</li><li>A communi observantia.</li><li>Cum ceteris in veneratione.</li><li>Quid securi etiam.</li><li>Hi omnes lingua, institutis.</li></ul>
  </div>
</footer>

<aside class="contact-widget">
  <h5>CONTACT US</h5>
  <p class="intro">We're not around right now. But you can send us an email and we'll get back to you, asap.</p>
  <div class="field first">Name*</div>
  <div class="field">Email*</div>
  <div class="field tall">Message*</div>
  <div class="field">Enter Captcha</div>
  <p class="refresh">Not readable? Change text.</p>
  <div class="captcha" role="img" aria-label="Distorted captcha word"></div>
  <div class="send">SEND</div>
</aside>

<a class="chat-btn"><svg width="13" height="10" viewBox="0 0 13 10"><rect width="13" height="10" fill="#fff"/><path d="M0 0l6.5 5.5L13 0" fill="none" stroke="#1e9be0" stroke-width="1.3"/></svg></a>
<svg class="to-top" width="10" height="8" viewBox="0 0 10 8"><path d="M1 6l4-4 4 4" fill="none" stroke="#fff" stroke-width="1.8"/></svg>

</body>
</html>
```